Architecture firm needing a business card

We need a business card design for a new company based in the US called "Pellmore Architecture". Seeking minimalist designs that have a creativity/design feel but must be clean and professional. Please refer to the logo attached.

Target Market(s)

Real Estate Investors, Home Builders and Construction Firms.

Industry/Entity Type

Architecture

Contact Information for Business Card

Standard US size business cards. Would like to have some sort of graphic on the back side of the card - nothing that is too loud but something that may catch your attention. More or less grayscale colors that are in line with the logo colors (navy and greys essentially). Additional colors maybe accepted if blended properly (earthtones), but might be difficult to accomplish and maintain the clean/minimalist look.

Requirements
Must have
• Clean Lines
Nice to have
• some sort of graphics, would like to have something creative on the back side of the card
Should not have
• nothing too busy, cluttered or overwhelming.

```html
<!DOCTYPE html>
<html lang="en">
<head>
<meta charset="utf-8">
<title>Pellmore Architecture — Business Card</title>
<link rel="stylesheet" href="https://fonts.googleapis.com/css2?family=Arimo:wght@400;700&display=swap">
<style>
  :root {
    --backdrop: #2b2b2d;
    --paper: #ffffff;
    --navy: #1f3f6e;
    --blue: #2e6bb0;
    --blue-light: #3c7fc6;
    --blue-deep: #0a1628;
    --ink: #3a3a3c;
    --ink-soft: #555558;
    --tile-grey: #dedede;
    --tile-navy: rgba(8, 22, 44, 0.55);
  }
  * { box-sizing: border-box; margin: 0; padding: 0; }
  html, body {
    width: 1200px; height: 1200px; overflow: hidden;
    background: var(--backdrop);
    font-family: "Arimo", Arial, sans-serif;
  }
  .canvas {
    width: 1200px; height: 1200px;
    display: flex; flex-direction: column; align-items: center; justify-content: center;
    gap: 60px;
  }
  .card {
    position: relative;
    width: 840px; height: 480px;
    overflow: hidden;
  }
  .card svg.card-art { position: absolute; inset: 0; }

  /* Contact side */
  .card--contact { background: var(--paper); }
  .holder {
    position: absolute; top: 12px; right: 372px;
    text-align: right; color: #fff;
  }
  .holder__name {
    font-size: 22px; letter-spacing: 2px;
    font-variant: small-caps; font-weight: 400;
  }
  .holder__role { font-size: 11px; font-weight: 700; margin-top: 2px; }

  .contact-list {
    position: absolute; left: 72px; top: 200px;
    list-style: none; display: flex; flex-direction: column; gap: 34px;
  }
  .contact-item { display: flex; align-items: center; gap: 30px; }
  .contact-item__icon { width: 50px; height: 50px; flex: none; }
  .contact-item__label { font-size: 27px; color: var(--ink); line-height: 1.1; }
  .contact-item__value { font-size: 14px; color: var(--ink-soft); margin-top: 3px; }

  /* Brand side */
  .card--brand {
    background: linear-gradient(125deg, var(--blue-light) 0%, var(--blue) 30%, #173766 65%, var(--blue-deep) 100%);
  }
  .brand-mark {
    position: absolute; left: 70px; top: 262px;
    display: flex; align-items: center; gap: 16px;
    color: #fff;
  }
  .brand-mark__square { width: 34px; height: 34px; background: #fff; }
  .brand-mark__name {
    font-size: 36px; font-weight: 700; letter-spacing: 1px;
    text-transform: uppercase; color: #fff;
  }
</style>
</head>
<body>
<main class="canvas">

  <section class="card card--contact" aria-label="Business card, contact side">
    <svg class="card-art" width="840" height="480" viewBox="0 0 840 480" aria-hidden="true">
      <defs>
        <linearGradient id="bandFill" x1="0" y1="0" x2="1" y2="0">
          <stop offset="0" stop-color="#2e6bb0"/>
          <stop offset="1" stop-color="#1f3f6e"/>
        </linearGradient>
      </defs>
      <polygon class="header-band" points="0,0 500,0 468,58 0,58" fill="url(#bandFill)"/>
      <polygon points="0,58 468,58 466,62 0,62" fill="#6e9bd0"/>
      <g class="tile-cluster" fill="var(--tile-grey)">
        <rect x="600" y="40" width="62" height="62" rx="6"/>
        <rect x="705" y="52" width="40" height="40" rx="4"/>
        <rect x="640" y="125" width="48" height="48" rx="5"/>
        <rect x="715" y="128" width="34" height="34" rx="4"/>
        <rect x="760" y="118" width="72" height="72" rx="7"/>
        <rect x="610" y="190" width="82" height="82" rx="7"/>
        <rect x="500" y="175" width="34" height="34" rx="3"/>
        <rect x="712" y="210" width="50" height="50" rx="5"/>
      </g>
    </svg>

    <div class="holder">
      <p class="holder__name">Lorem Ipsum</p>
      <p class="holder__role">Director</p>
    </div>

    <ul class="contact-list">
      <li class="contact-item">
        <svg class="contact-item__icon" viewBox="0 0 50 50" aria-hidden="true">
          <rect width="50" height="50" rx="8" fill="var(--navy)"/>
          <path d="M17 13c2 0 3 3 4 6 0 1-2 2-2 3 1 3 4 6 7 7 1 0 2-2 3-2 3 1 6 2 6 4 0 2-3 5-6 5-9-1-17-9-18-18 0-3 3-5 6-5z" fill="#fff"/>
        </svg>
        <div>
          <p class="contact-item__label">Phone number</p>
          <p class="contact-item__value">+1 555 014 2290</p>
        </div>
      </li>
      <li class="contact-item">
        <svg class="contact-item__icon" viewBox="0 0 50 50" aria-hidden="true">
          <circle cx="25" cy="25" r="22" fill="var(--navy)"/>
          <circle cx="25" cy="25" r="14" fill="none" stroke="#fff" stroke-width="2.5"/>
          <ellipse cx="25" cy="25" rx="6" ry="14" fill="none" stroke="#fff" stroke-width="2"/>
          <line x1="11" y1="25" x2="39" y2="25" stroke="#fff" stroke-width="2"/>
        </svg>
        <div>
          <p class="contact-item__label">Your email</p>
          <p class="contact-item__value">+1 555 014 2290</p>
        </div>
      </li>
      <li class="contact-item">
        <svg class="contact-item__icon" viewBox="0 0 50 50" aria-hidden="true">
          <polygon points="5,10 18,5 32,10 45,5 45,40 32,45 18,40 5,45" fill="var(--navy)"/>
          <line x1="18" y1="5" x2="18" y2="40" stroke="#fff" stroke-width="2"/>
          <line x1="32" y1="10" x2="32" y2="45" stroke="#fff" stroke-width="2"/>
        </svg>
        <div>
          <p class="contact-item__label">Street address</p>
          <p class="contact-item__value">+1 555 014 2290</p>
        </div>
      </li>
    </ul>
  </section>

  <section class="card card--brand" aria-label="Business card, brand side">
    <svg class="card-art" width="840" height="480" viewBox="0 0 840 480" aria-hidden="true">
      <g class="tile-cluster" fill="var(--tile-navy)">
        <rect x="640" y="40" width="70" height="70" rx="6"/>
        <rect x="735" y="58" width="40" height="40" rx="4"/>
        <rect x="650" y="130" width="52" height="52" rx="5"/>
        <rect x="725" y="138" width="36" height="36" rx="4"/>
        <rect x="770" y="125" width="62" height="62" rx="6"/>
        <rect x="640" y="200" width="82" height="82" rx="7"/>
        <rect x="520" y="185" width="34" height="34" rx="3"/>
      </g>
    </svg>
    <div class="brand-mark">
      <span class="brand-mark__square" aria-hidden="true"></span>
      <span class="brand-mark__name">Pellmore Architecture</span>
    </div>
  </section>

</main>
</body>
</html>
```